Website Design for my CNC machine Shop.

I need a new website for my Machining Company.

It can be a simple website that acts more like an "Online Business card" I has to highlight the services I provide and give Companies the confidence to engage my services.

I needs it to be a really modern or even a little futuristic promoting my Company.

I have just moved locations and have renovated the premises and would be great to let everyone know along with a new website.

If you can help with linking it to search engines to help get more exposure that would be great.

It needs to accommodate the three main services I provide which will include capacities of each machine (within that service) and maybe a couple images.
CNC Machining (5-axis, 3-axis)
EDM Wire cutting
3D Metal Printing
Along with home page and Contact page

I have two websites and you can use the txt from either/combination of these.
www.korvaltooling.com.au
(no longer do Laser Marking and etching but now do 3D metal Printing)
www.tarnquill.com.au

Happy to chat further with the designer

Company logo's provided.

For Images: I am happy to use Glimmerbay and can purchase any images you like
EDM Wire cut
https://www.glimmerbay-pics.com/search/edm-wire-cutting

CNC Machining:
https://www.glimmerbay-pics.com/search/vertical-cnc-machining
Don't use any with engines or motor vehicle parts

3D metal Printing
https://www.glimmerbay-pics.com/search/slm-metal-printing

Target Market(s)

Defence, Aerospace, Medical, HIgh Precision

Industry/Entity Type

Mechanical Engineering

Coding

Coded - Design and coding required

Number of Pages Required

5+ page

Requirements
Must have
• Home page, 3 services, Contacts. Can add image to each of the services

```html
<!DOCTYPE html>
<html lang="en">
<head>
<meta charset="utf-8">
<title>Korval Precision Machinery – Website Pages</title>
<link href="https://fonts.googleapis.com/css2?family=Outfit:wght@300;400;500;600;700&display=swap" rel="stylesheet">
<style>
  :root{
    --stage:#3f4c6e;
    --white:#ffffff;
    --ink:#1b1d22;
    --muted:#6f7a86;
    --blue:#4a7ae6;
    --blue-deep:#2f5fcc;
    --red:#d93a3a;
    --black:#0a0a0b;
    --hero-a:#0d1420;
    --hero-b:#243b5c;
    --hero-c:#c98a3a;
    --blueprint-a:#3a3835;
    --blueprint-b:#6b5a44;
    --card:#0e0f11;
    --photo-a:#1e4a72;
    --photo-b:#8fb3cf;
  }
  *{box-sizing:border-box;margin:0;padding:0}
  html,body{width:1200px;height:732px;overflow:hidden}
  body{background:var(--stage);font-family:'Outfit',sans-serif;position:relative;color:var(--white)}

  .page{position:absolute;width:570px;background:var(--white);box-shadow:0 6px 18px rgba(0,0,0,.35);overflow:hidden}
  .page--home{left:20px;top:40px;height:320px}
  .page--service{left:610px;top:40px;height:544px}

  .site-header{position:absolute;left:0;top:0;width:100%;height:45px;background:var(--white);text-align:center}
  .brand{position:absolute;left:0;right:0;top:8px;text-align:center;font-weight:500;font-size:12px;color:var(--ink);line-height:1}
  .nav{position:absolute;left:0;right:0;top:28px;display:flex;justify-content:center;gap:17px;font-size:5.6px;color:var(--ink)}
  .nav .is-active{color:var(--blue);text-decoration:underline}

  .hero{position:absolute;left:0;top:45px;width:100%;height:243px;
    background:radial-gradient(circle at 62% 72%, var(--hero-c) 0, rgba(201,138,58,.25) 7%, transparent 16%),
               linear-gradient(115deg,var(--hero-a) 0 38%,var(--hero-b) 55%,var(--hero-a) 72%,#151a22 100%)}
  .hero__title{position:absolute;left:63px;top:36px;font-size:12.4px;font-weight:600;line-height:1.25;width:300px}
  .hl{color:var(--blue)}
  .hero__text{position:absolute;left:63px;top:74px;width:172px;font-size:5.5px;line-height:1.4;font-weight:400}
  .search{position:absolute;left:63px;top:111px;width:118px;height:17px;background:var(--white);border-radius:3px;color:var(--muted);font-size:5.4px;padding:5px 5px}
  .search svg{position:absolute;right:4px;top:5px}
  .btn{position:absolute;height:15px;border-radius:8px;background:var(--blue);color:var(--white);font-size:5.4px;display:flex;align-items:center;justify-content:center}

  .site-footer{position:absolute;left:0;width:100%;background:var(--black);color:#cfd3d8;font-size:3.8px;line-height:1.5}
  .site-footer a{color:#cfd3d8}
  .page--home .site-footer{top:303px;height:17px;padding:3px 0 0 64px}
  .page--service .site-footer{top:524px;height:20px;padding:4px 0 0;text-align:center}

  .services-banner{position:absolute;left:0;top:45px;width:100%;height:182px;
    background:linear-gradient(110deg,var(--blueprint-a),#2b2a29 45%,var(--blueprint-b) 70%,#2c2c2c)}
  .badge{position:absolute;left:99px;top:18px;width:116px;height:25px;background:var(--red);border-radius:2px;display:flex;align-items:center;justify-content:center;gap:4px;font-size:12px;font-weight:500;letter-spacing:.4px}
  .badge small{font-size:4.5px}
  .services-banner__title{position:absolute;left:99px;top:51px;font-size:11.6px;font-weight:500}
  .services-banner__text{position:absolute;left:99px;top:73px;width:258px;font-size:5.4px;line-height:1.5;font-weight:300}
  .gears{position:absolute;left:440px;top:16px}
  .tabs{position:absolute;left:0;top:151px;width:100%;font-size:8.6px;font-weight:300}
  .tabs span{position:absolute}
  .tabs .is-active{color:var(--blue);text-decoration:underline}

  .service-card{position:absolute;left:58px;top:239px;width:453px;height:267px;background:var(--card);border-radius:5px;overflow:hidden}
  .service-card__title{position:absolute;left:40px;top:36px;font-size:11px;font-weight:500;border-bottom:1.2px solid var(--blue);padding-bottom:1px}
  .service-card__text{position:absolute;left:40px;top:59px;width:216px;font-size:5.6px;line-height:1.55;letter-spacing:.15px}
  .photo{position:absolute;background:linear-gradient(135deg,var(--photo-a),var(--photo-b) 55%,var(--photo-a))}
  .photo--feature{left:295px;top:18px;width:119px;height:121px;background:linear-gradient(140deg,#222,#8a8d90 50%,#1b1b1b)}
</style>
</head>
<body>

<section class="page page--home" aria-label="Home page">
  <header class="site-header">
    <div class="brand">Korval</div>
    <nav class="nav">
      <span class="is-active">HOME</span><span>CNC MACHINING</span><span>EDM WIRE CUTTING</span><span>3D METAL PRINTING</span><span>CONTACT</span>
    </nav>
  </header>

  <div class="hero" role="img" aria-label="Laser cutting head sending sparks across a metal sheet beside a CNC spindle">
    <h1 class="hero__title">Precision Engineering Solutions: Revolutionizing <span class="hl">Manufacturing</span> with Cutting-Edge <span class="hl">Technology</span></h1>
    <p class="hero__text">Our core sectors of expertise are in EDM wire cutting, 3D Metal Printing and CNC machining. With our combination of highly skilled staff and sophisticated machinery we offer a comprehensive and professional service.</p>
    <div class="search">Search...
      <svg width="6" height="6" viewBox="0 0 10 10"><circle cx="4" cy="4" r="3" fill="none" stroke="#9aa2ab" stroke-width="1.2"/><line x1="6.3" y1="6.3" x2="9" y2="9" stroke="#9aa2ab" stroke-width="1.2"/></svg>
    </div>
    <span class="btn" style="left:63px;top:138px;width:57px">OUR SERVICES</span>
    <span class="btn" style="left:127px;top:138px;width:53px">CONTACT US</span>
  </div>

  <footer class="site-footer">
    Copyright © 2024 KORVAL PRECISION MACHINERY . All rights reserved.<br>
    <a href="#">Privacy Policy</a> | <a href="#">Terms of Use</a>
  </footer>
</section>

<section class="page page--service" aria-label="CNC machining service page">
  <header class="site-header">
    <div class="brand">Korval</div>
    <nav class="nav">
      <span>HOME</span><span class="is-active">CNC MACHINING</span><span>EDM WIRE CUTTING</span><span>3D METAL PRINTING</span><span>CONTACT</span>
    </nav>
  </header>

  <div class="services-banner" role="img" aria-label="Engineering drawings with a magnifying glass and ruler">
    <div class="badge">SERVICES <small>NO.1</small></div>
    <h2 class="services-banner__title">Unparalleled Solutions for Your <span class="hl">Unique Needs</span></h2>
    <p class="services-banner__text">Our services stand out through a perfect blend of cutting-edge technology and personalized customer care, ensuring each client receives tailored solutions that exceed expectations.</p>
    <span class="btn" style="left:99px;top:98px;width:52px;height:16px">CONTACT US</span>
    <svg class="gears" width="32" height="28" viewBox="0 0 32 28" aria-hidden="true">
      <g fill="none" stroke="var(--blue-deep)">
        <circle cx="11" cy="12" r="6" stroke-width="4" stroke-dasharray="3 2"/>
        <circle cx="11" cy="12" r="3.5" stroke-width="2.5"/>
        <circle cx="24" cy="20" r="3.5" stroke-width="3" stroke-dasharray="2 1.5"/>
        <circle cx="25" cy="6" r="2.5" stroke-width="2.5" stroke-dasharray="1.6 1.2"/>
      </g>
    </svg>
    <div class="tabs">
      <span class="is-active" style="left:108px">CNC MACHINING</span>
      <span style="left:243px">EDM WIRE CUTTING</span>
      <span style="left:374px">3D METAL PRINTING</span>
    </div>
  </div>

  <article class="service-card">
    <h3 class="service-card__title">CNC 3/5 AXIS MACHINING</h3>
    <p class="service-card__text">OUR CNC 3-5 AXIS MACHINING SERVICE OFFERS UNPARALLELED PRECISION AND EFFICIENCY FOR A WIDE RANGE OF MANUFACTURING NEEDS. UTILIZING ADVANCED COMPUTER NUMERICAL CONTROL TECHNOLOGY, OUR 3-AXIS MACHINING CAPABILITIES ENABLE US TO PRODUCE COMPLEX AND INTRICATE PARTS WITH EXCEPTIONAL ACCURACY.</p>
    <div class="photo photo--feature" role="img" aria-label="Machined aluminium part on a CNC rotary table"></div>
    <div class="photo" style="left:40px;top:155px;width:119px;height:93px" role="img" aria-label="CNC readout over a milling cutter in blue tone"></div>
    <div class="photo" style="left:168px;top:155px;width:119px;height:93px" role="img" aria-label="End mill cutting an aluminium block in blue tone"></div>
    <div class="photo" style="left:295px;top:155px;width:119px;height:93px" role="img" aria-label="Lathe chuck holding a machined part in blue tone"></div>
  </article>

  <footer class="site-footer">
    Copyright © 2024 KORVAL PRECISION MACHINERY . All rights reserved.<br>
    <a href="#">Privacy Policy</a> | <a href="#">Terms of Use</a>
  </footer>
</section>

</body>
</html>
```